Reggie Vosburn - Free Personalised Health Consultation - "Every body walks its own path"

This flyer will be left on tables/seats at speaking events and seminars and used to attain leads.

Top half will have "SMS me for a FREE Personalised Health Consultation" and my picture (see www.reggievosburn.example and pick most engaging photo) and underneath my contact details. It must have lines with "Notes:" halfway down so people can take notes at the seminar and lines on the back with my contact details again and "Notes: with lines.

I am having a business card also being designed by Plotnest for same and would like the flyer and business card to carry a similar feel/look for consistency.

Below is the brief for the business card being designed:
Business Card for www.reggievosburn.example site. It is a trust site and I use it for 1:1 relatable connections. It is the one I use for building intimate 1:1 trust building and Exec Coaching Services and programs for high wealth individuals and corporates. I also have a commercial programmatic site of my personal health products and services and programs for main stream one to many. www.crossgenvitality.example that can also provoke thought for the www.reggievosburn.example business card. (mind you will get a separate business card for that site, but want to provide context). It has a logo which you may want to draw from in designing the reggievosburn business card which is personal and is about building my brand. There is also a reggievosburn personal KX page and reggievosburn business KX page. I am a Certified Talent Compass 4.1 Coach with Verrick and you can get a corporate brief of me on there to give you more context https://www.verricktalenthub.example/coach/en-us/directory?search=reggie

Target Market(s)

Exec, IT, Health conscious. Corporates wanting to run Health and Wellness programs. Those wanting to go from good to great. Millennials to Middleaged.

Industry/Entity Type

Health And Wellness

Font styles to use
Sans Serif
Other font styles liked:
• Arial and Calibri ok too

Colors

Designer to choose colors to be used in the design.

Requirements
Must have
• Picture of me - use best from www.reggievosburn.example or can send one you choose.
• Contact details like my buisness card being designed by you guys in separate project.
• Name: Reggie Vosburn
• email: reggie@reggievosburn.,example
• Phone: Australia +61 455 318 026 Singapore: +65 8342 1960
Nice to have
• Open to ideas

```html
<!DOCTYPE html>
<html lang="en">
<head>
<meta charset="utf-8">
<title>Reggie Vosburn – Seminar Notes Flyer</title>
<link href="https://fonts.googleapis.com/css2?family=Poppins:wght@500;600;700;800&display=swap" rel="stylesheet">
<style>
  :root {
    --backdrop: #838a8b;
    --paper: #ffffff;
    --panel: #b5b9b9;
    --ink: #000000;
    --rule: #c4c6c6;
    --footer-ink: #7d8283;
    --photo-dark: #2a2a2a;
    --photo-light: #8c8c8c;
  }
  * { margin: 0; padding: 0; box-sizing: border-box; }
  html, body {
    width: 1200px; height: 1006px; overflow: hidden;
    background: var(--backdrop);
    font-family: "Poppins", Arial, sans-serif;
  }
  .page {
    position: absolute;
    background: var(--paper);
  }
  .page--back { left: 60px; top: 99px; width: 531px; height: 755px; }
  .page--front { left: 608px; top: 100px; width: 530px; height: 753px; }

  .notes-label {
    position: absolute;
    font-weight: 700; font-size: 17.5px; color: var(--ink);
    line-height: 1;
  }
  .ruled {
    position: absolute;
    background: repeating-linear-gradient(to bottom,
      var(--rule) 0, var(--rule) 1px, transparent 1px, transparent 21px);
  }
  .page--back .notes-label { left: 26px; top: 41px; }
  .page--back .ruled { left: 26px; top: 74px; width: 478px; height: 589px; }

  .back-footer {
    position: absolute; right: 27px; top: 674px;
    text-align: right; color: var(--footer-ink);
    font-weight: 600; font-size: 12.8px; line-height: 17.8px;
    white-space: nowrap;
  }

  .promo {
    position: absolute; left: 27px; top: 0; width: 478px; height: 360px;
    background: var(--panel);
  }
  .promo__photo {
    position: absolute; left: 31px; top: 0; width: 189px; height: 184px;
    background: linear-gradient(160deg, var(--photo-light) 0%, #5a5a5a 45%, var(--photo-dark) 100%);
  }
  .promo__headline {
    position: absolute; right: 33px; top: 38px;
    color: var(--paper); font-weight: 700; font-size: 104px;
    line-height: 70px; text-align: center; letter-spacing: -2px;
  }
  .promo__headline span { display: block; }
  .promo__offer {
    position: absolute; left: 0; width: 100%; top: 198px;
    text-align: center; color: var(--ink);
    font-weight: 600; font-size: 35px; line-height: 35px;
    white-space: nowrap;
  }
  .promo__contact {
    position: absolute; left: 0; width: 100%; top: 274px;
    text-align: center; color: var(--paper);
    font-weight: 600; font-size: 34.5px; line-height: 35px;
    white-space: nowrap;
  }
  .divider {
    position: absolute; left: 27px; top: 378px; width: 478px; height: 9px;
    background: var(--ink);
  }
  .page--front .notes-label { left: 27px; top: 400px; }
  .page--front .ruled { left: 27px; top: 426px; width: 478px; height: 295px; }
</style>
</head>
<body>
  <section class="page page--back">
    <h2 class="notes-label">Notes</h2>
    <div class="ruled"></div>
    <div class="back-footer">
      <p>reggievosburn.example</p>
      <p>e: reggie@reggievosburn.example</p>
      <p>Australia +61 455318026&nbsp; Singapore +65 83421960</p>
    </div>
  </section>

  <section class="page page--front">
    <div class="promo">
      <div class="promo__photo" role="img" aria-label="Black and white portrait of Reggie Vosburn seated on a leather sofa, gesturing warmly"></div>
      <h1 class="promo__headline"><span>SMS</span><span>me</span></h1>
      <p class="promo__offer">for a FREE Personalised<br>Health Consultation</p>
      <p class="promo__contact">Australia +61 455318026<br>Singapore +65 83421960</p>
    </div>
    <div class="divider"></div>
    <h2 class="notes-label">Notes</h2>
    <div class="ruled"></div>
  </section>
</body>
</html>
```